Strength Coach Business Card Design Project

I would like a business card design to complement my new logo. I would like the card to be clean, seek and strong!

Target Market(s)

Mostly adults and junior atheletes who are serious about changing their lives.

Industry/Entity Type

Business

Font styles to use
Serif

Colors

Designer to choose colors to be used in the design.

```html
<!DOCTYPE html>
<html lang="en">
<head>
<meta charset="utf-8">
<title>Ridge Strength and Fitness – Business Cards</title>
<link href="https://fonts.googleapis.com/css2?family=Open+Sans:wght@400;700&display=swap" rel="stylesheet">
<style>
  :root {
    --stage: #1b1b1b;
    --card-black: #141414;
    --card-black-soft: #242424;
    --brand-red: #dc2a22;
    --brand-red-deep: #b81d17;
    --white: #ffffff;
    --muted: #f1f1f1;
  }
  * { margin: 0; padding: 0; box-sizing: border-box; }
  html, body {
    width: 1200px; height: 944px; overflow: hidden;
    background: var(--stage);
    font-family: "Open Sans", sans-serif;
  }
  .stage { position: relative; width: 1200px; height: 944px; }
  .card {
    position: absolute; left: 250px; width: 700px; height: 400px;
    background: linear-gradient(135deg, var(--card-black-soft), var(--card-black) 60%);
    overflow: hidden;
    box-shadow: 0 18px 40px rgba(0,0,0,.55);
  }
  .card-front { top: 52px; }
  .card-back { top: 492px; }

  .brand {
    display: flex; align-items: center; gap: 14px;
    color: var(--white); font-weight: 700;
  }
  .brand-mark { width: 22px; height: 22px; background: var(--brand-red); flex: none; }
  .brand-name {
    font-size: 34px; line-height: 1.05; letter-spacing: 1px; text-transform: uppercase;
  }
  .card-front .brand {
    position: absolute; left: 50%; top: 50%; transform: translate(-50%, -50%);
  }
  .card-back .brand { position: absolute; left: 44px; top: 48px; }
  .card-back .brand-name { font-size: 26px; }

  .contact-list { position: absolute; left: 44px; top: 190px; list-style: none; }
  .contact-item {
    display: flex; align-items: center; gap: 14px;
    color: var(--white); font-size: 19px; margin-bottom: 14px;
  }
  .contact-icon { width: 20px; height: 20px; fill: var(--brand-red); flex: none; }

  .wave { position: absolute; inset: 0; width: 700px; height: 400px; }

  .holder {
    position: absolute; right: 40px; top: 200px; text-align: right; color: var(--white);
  }
  .holder-name { font-size: 22px; font-weight: 700; line-height: 1.2; }
  .holder-role { font-size: 16px; color: var(--muted); margin-top: 4px; }
</style>
</head>
<body>
<main class="stage">

  <section class="card card-front">
    <div class="brand">
      <span class="brand-mark"></span>
      <span class="brand-name">Ridge Strength<br>and Fitness</span>
    </div>
  </section>

  <section class="card card-back">
    <svg class="wave" viewBox="0 0 700 400" aria-hidden="true">
      <path d="M700 14 C550 36 450 110 395 185 C330 275 220 320 0 325 L0 338 C228 334 340 288 405 196 C460 120 560 52 700 30 Z" fill="var(--white)"/>
      <path d="M700 50 C560 70 470 130 420 200 C355 292 240 348 0 352 L0 400 L700 400 Z" fill="var(--brand-red)"/>
      <path d="M700 50 C640 62 600 90 570 120 L700 400 Z" fill="var(--brand-red-deep)" opacity=".25"/>
    </svg>

    <div class="brand">
      <span class="brand-mark"></span>
      <span class="brand-name">Ridge Strength<br>and Fitness</span>
    </div>

    <ul class="contact-list">
      <li class="contact-item">
        <svg class="contact-icon" viewBox="0 0 24 24"><path d="M6.6 10.8a15.1 15.1 0 0 0 6.6 6.6l2.2-2.2a1 1 0 0 1 1-.25 11.4 11.4 0 0 0 3.6.57 1 1 0 0 1 1 1V20a1 1 0 0 1-1 1A17 17 0 0 1 3 4a1 1 0 0 1 1-1h3.5a1 1 0 0 1 1 1c0 1.25.2 2.45.57 3.6a1 1 0 0 1-.25 1z"/></svg>
        <span>0400 123 987</span>
      </li>
      <li class="contact-item">
        <svg class="contact-icon" viewBox="0 0 24 24"><path d="M2 5h20v14H2z M3 6l9 7 9-7" stroke="var(--card-black)" stroke-width="1.4"/></svg>
        <span>coach@ridge-coach.co</span>
      </li>
      <li class="contact-item">
        <svg class="contact-icon" viewBox="0 0 24 24"><circle cx="12" cy="12" r="10"/><path d="M2 12h20M12 2c3 3 3 17 0 20M12 2c-3 3-3 17 0 20" stroke="var(--card-black)" stroke-width="1.2" fill="none"/></svg>
        <span>www.ridge-coach.co</span>
      </li>
    </ul>

    <div class="holder">
      <p class="holder-name">Marcus Ridge</p>
      <p class="holder-role">Strength and Fitness Coach</p>
    </div>
  </section>

</main>
</body>
</html>
```